Loomberry AI - Help users create their own recipe for a delicious AI treat!

Our company is an AI startup called Loomberrys. A Loomberry is an easy way to play with data (user can ask questions and get visualized answers about the dataset, sort of like QuillMate). Our users can "bake" their own Loomberrys by combining different sources of data.

We need a page that offers two things (both are required):

(1) TRY A LOOMBERRY --> Present a gallery of pre-made Loomberrys, each of which a user can click on and start playing with inside a popup iFrame. (visually, a Loomberry should be represented by some variation of our logo, attached). Designer does not need to worry about the iFrame popup.

(2) BAKE YOUR OWN LOOMBERRY --> Guide the user through making their own Loomberry recipe. The steps in making a Loomberry are:

A. Pick first ingredient - a Connector that imports the user's own data (visually, we present these options as logos for the Connector source, like Zentor, plain circle, Brivane KLX, etc.).

B. Pick additional ingredients - the user can choose from 3rd-party cakes to combine with their own data added in (A). (visually, these 3rd-party cake options are presented as "mini" cakes, similar to our logo)

C. Once the ingredients are selected, the user can hit a BAKE button, and an iFrame popup opens, where user can play with the result. Designer does not need to worry about the iFrame popup.

We already have a web page and color scheme that we'd like this page to match (https://www.loomberrys.ai). The designer has freedom to play with format and try variations on the color scheme. The overall design should feel futuristic, fun, but also professional (like our logo).

Target Market(s)

Business users who want an easier way to get answers from large messy data

Industry/Entity Type

Tech/AI

Number of Pages Required

1 page

Font styles to use
Other font styles liked:
• Rubik

Requirements
Must have
• Full page design that matches current website (www.loomberrys.ai) and meets all requirements in the Project Description
Nice to have
• Included in the Project Description
Should not have
• Do not submit any designs that are too cartoonish or would not appeal to a business user

```html
<!DOCTYPE html>
<html lang="en">
<head>
<meta charset="utf-8">
<title>Loomberrys – Try or Bake a Loomberry</title>
<link href="https://fonts.googleapis.com/css2?family=Rubik:wght@400;500;600;700&display=swap" rel="stylesheet">
<style>
:root{
  --ink:#16161d;
  --muted:#3b3b46;
  --line:#d9d3d8;
  --yellow:#f7e84a;
  --pink:#e77fc3;
  --cyan:#17e2f6;
  --blue:#0d4fa6;
  --red:#e5232c;
  --violet:#7a6fd6;
}
*{box-sizing:border-box;margin:0;padding:0}
html,body{width:1200px;height:4677px;overflow:hidden}
body{
  position:relative;font-family:"Rubik",sans-serif;color:var(--ink);
  background:
    radial-gradient(520px 420px at 720px 480px,rgba(250,233,140,.55),transparent 70%),
    radial-gradient(520px 520px at 1050px 120px,rgba(250,200,230,.45),transparent 70%),
    radial-gradient(600px 500px at 1180px 1400px,rgba(250,240,160,.45),transparent 70%),
    radial-gradient(600px 600px at 0 2200px,rgba(250,190,225,.5),transparent 70%),
    radial-gradient(600px 600px at 1200px 2900px,rgba(170,190,250,.55),transparent 70%),
    radial-gradient(560px 560px at 0 4200px,rgba(170,190,250,.5),transparent 70%),
    radial-gradient(560px 560px at 1100px 3750px,rgba(250,190,225,.5),transparent 70%),
    radial-gradient(560px 400px at 1000px 4650px,rgba(250,236,160,.5),transparent 70%),
    #fff;
}
.abs{position:absolute}
.grad{background:linear-gradient(90deg,var(--yellow),var(--pink) 55%,var(--cyan))}
.brand{display:flex;align-items:center;gap:12px}
.brand-mark{width:30px;height:30px;border-radius:6px;border:3px solid var(--pink)}
.brand-name{font-size:30px;font-weight:400;color:var(--violet)}
.nav a{position:absolute;top:46px;font-size:13px;color:var(--ink);text-decoration:none}
.btn-outline{border:1.5px solid var(--ink);border-radius:30px;display:flex;align-items:center;justify-content:center;font-size:12px;font-weight:600;background:transparent}
.waitlist{border-color:var(--blue);color:var(--blue)}
.hero-title{font-size:39px;font-weight:500;line-height:53px}
.small{font-size:12.5px;line-height:17px;color:var(--muted)}
.section-title{text-align:center;font-weight:500}
.divider{height:2px;background:var(--ink);width:132px;left:534px}
.card{border:1px solid #ecdfe3;border-radius:22px;background:rgba(255,255,255,.35);width:332px;height:237px}
.card .mark{position:absolute;left:44px;top:42px;width:62px;height:62px;border-radius:10px;border:4px solid var(--pink);background:linear-gradient(135deg,rgba(247,232,74,.35),rgba(23,226,246,.35))}
.card p{position:absolute;left:26px;right:70px;bottom:36px;font-size:15.5px;font-weight:500;line-height:21px}
.step-label{font-size:11px;letter-spacing:2px;color:var(--muted)}
.step-title{font-size:30px;font-weight:500;line-height:33px}
.pill{border-radius:90px;overflow:hidden}
.block{border-radius:20px}
.choice{border-radius:30px;display:flex;align-items:center;justify-content:center;font-size:20px;font-weight:600;background:#fff;box-shadow:0 3px 10px rgba(0,0,0,.12)}
.solid{border-radius:30px;display:flex;align-items:center;justify-content:center;font-size:12.5px;font-weight:600;color:#fff}
.faq{border:1.5px solid #2a2a35;border-radius:6px;background:rgba(255,255,255,.4);left:329px;width:540px;font-size:10.5px;font-weight:500;padding:0 18px}
.faq .q{display:flex;justify-content:space-between;align-items:center;height:44px}
.faq .sign{width:16px;height:16px;border-radius:50%;background:#f0ecf2;display:flex;align-items:center;justify-content:center;font-size:11px}
.field{left:329px;width:540px;border:1.5px solid #2a2a35;border-radius:6px;font-size:10.5px;letter-spacing:1px;color:var(--muted);padding:0 18px;display:flex;align-items:center;background:rgba(255,255,255,.3)}
.foot h4{font-size:16px;font-weight:600}
.foot a{font-size:11.5px;color:var(--ink);text-decoration:none}
</style>
</head>
<body>

<!-- Header -->
<div class="abs brand" style="left:87px;top:36px"><span class="brand-mark"></span><span class="brand-name">loomberrys</span></div>
<nav class="nav">
  <a style="left:434px">Home</a><a style="left:511px">About Us</a><a style="left:609px">Web Demo</a><a style="left:716px">Contact</a>
</nav>
<div class="abs btn-outline waitlist" style="left:958px;top:34px;width:158px;height:40px">Join the WaitList</div>

<!-- Hero -->
<p class="abs" style="left:84px;top:170px;font-size:12.5px">Welcome to Loomberrys!</p>
<h1 class="abs hero-title" style="left:84px;top:210px">Does Your Company<br>Have Data That Others Would<br>Find Useful?</h1>
<p class="abs small" style="left:84px;top:435px;width:540px">Explore our pre-made Loomberrys and dive into the world of data visualization. Click on any Loomberry below to start playing!</p>
<div class="abs grad solid" style="left:84px;top:508px;width:174px;height:44px;justify-content:flex-start;padding-left:14px;font-size:11px">TRY A LOOMBERRY
  <span style="position:absolute;right:12px;width:26px;height:26px;border-radius:50%;background:#fff;display:flex;align-items:center;justify-content:center">
    <svg width="14" height="14" viewBox="0 0 14 14"><path d="M2 7h9M7 3l4 4-4 4" stroke="#5fa7e8" stroke-width="1.8" fill="none"/></svg></span></div>
<div class="abs btn-outline" style="left:294px;top:508px;width:209px;height:44px">BAKE YOUR OWN LOOMBERRY</div>
<div class="abs" role="img" aria-label="Photo of a team working together at computers" style="left:695px;top:327px;width:421px;height:266px;border-radius:12px;background:linear-gradient(135deg,#5c6a7a,#2b2f3a 55%,#8a6a55);display:flex;align-items:center;justify-content:center">
  <svg width="38" height="38" viewBox="0 0 38 38"><circle cx="19" cy="19" r="19" fill="rgba(255,255,255,.85)"/><path d="M15 11l12 8-12 8z" fill="#2aa3e6"/></svg>
</div>

<!-- Gallery -->
<h2 class="abs section-title" style="left:0;width:1200px;top:716px;font-size:25px;line-height:42px">Discover The Magic Of Data Visualization With Our Pre-Made Loomberrys.<br>Simply Click On A Loomberry Below To Start Exploring.</h2>
<div class="abs divider" style="top:817px"></div>

<div class="abs card" style="left:84px;top:858px"><span class="mark"></span><p>Who are our repeat customers and how many times have they shopped with us?</p></div>
<div class="abs card" style="left:434px;top:858px"><span class="mark"></span><p>Show me all outstanding invoices by due date</p></div>
<div class="abs card" style="left:782px;top:858px"><span class="mark"></span><p>Show me all credit card expenses over $100</p></div>
<div class="abs card" style="left:84px;top:1125px"><span class="mark"></span><p>Show me all credit card expenses over $100</p></div>
<div class="abs card" style="left:434px;top:1125px"><span class="mark"></span><p>How much are our monthly expenses on average?</p></div>
<div class="abs card" style="left:782px;top:1125px"><span class="mark"></span><p>What's the total amount invoiced by customer zip code?</p></div>
<div class="abs btn-outline" style="left:537px;top:1408px;width:125px;height:30px;font-size:11px">View More</div>

<!-- Bake your own -->
<h2 class="abs section-title" style="left:0;width:1200px;top:1505px;font-size:38px;font-weight:600">BAKE YOUR OWN LOOMBERRY</h2>
<div class="abs divider" style="top:1581px"></div>

<!-- Step 1 -->
<p class="abs step-label" style="left:171px;top:1692px">STEP- 1</p>
<h3 class="abs step-title" style="left:171px;top:1725px">Pick First Ingredient</h3>
<p class="abs small" style="left:171px;top:1784px;width:410px;font-size:11.5px">Choose a connector to import your own data seamlessly. Select from popular options:</p>
<div class="abs choice" style="left:171px;top:1864px;width:158px;height:38px;color:#4a74d9;font-weight:500">Zentor</div>
<div class="abs choice" style="left:345px;top:1864px;width:158px;height:38px">brivane</div>
<div class="abs solid" style="left:171px;top:1935px;width:158px;height:38px;background:var(--blue)">Connect Your OWN</div>

<div class="abs block" style="left:639px;top:1821px;width:388px;height:237px;background:linear-gradient(135deg,var(--yellow),var(--pink) 50%,var(--cyan))"></div>
<div class="abs pill" role="img" aria-label="Dashboard screen with blue bar charts" style="left:608px;top:1634px;width:162px;height:328px;background:linear-gradient(180deg,#0f3a2a,#05080c 30%,#0a2e4a 60%,#05080c)"></div>
<div class="abs pill" role="img" aria-label="Dashboard screen with analytics charts" style="left:795px;top:1683px;width:162px;height:326px;background:linear-gradient(180deg,#05080c,#0a3a4a 45%,#05080c 75%,#0b1a14)"></div>

<svg class="abs" style="left:470px;top:2000px" width="290" height="220" viewBox="0 0 290 220" fill="none" stroke="#2a2a35" stroke-width="1.5">
  <path d="M8 6C8 120 80 120 180 110C250 104 280 150 280 208"/><path d="M274 200l6 10 6-10"/>
</svg>

<!-- Step 2 -->
<div class="abs block" style="left:201px;top:2272px;width:391px;height:293px;background:linear-gradient(225deg,var(--yellow),var(--pink) 50%,var(--cyan))"></div>
<div class="abs pill" role="img" aria-label="Server room with blue lights" style="left:156px;top:2165px;width:167px;height:325px;background:linear-gradient(180deg,#0a1a3a,#1f6fd6 50%,#050a18)"></div>
<div class="abs pill" role="img" aria-label="Server racks with blue lights" style="left:348px;top:2214px;width:171px;height:325px;background:linear-gradient(180deg,#050a18,#2a86e8 50%,#0a1a3a)"></div>
<p class="abs step-label" style="left:608px;top:2216px">STEP-2</p>
<h3 class="abs step-title" style="left:608px;top:2243px">Pick Additional Ingredients -<br>3rd-Party Cakes</h3>
<p class="abs small" style="left:608px;top:2330px;width:440px;font-size:11.5px">Enhance your data with a variety of 3rd-party cakes. Mix and match to create your perfect recipe:</p>
<div class="abs solid" style="left:608px;top:2414px;width:158px;height:36px;background:var(--blue)">Nation Tally</div>
<div class="abs solid" style="left:782px;top:2414px;width:158px;height:36px;background:var(--red)">Your Interest</div>

<svg class="abs" style="left:470px;top:2540px" width="290" height="222" viewBox="0 0 290 222" fill="none" stroke="#2a2a35" stroke-width="1.5">
  <path d="M280 6C280 120 210 120 110 112C40 106 8 150 8 212"/><path d="M2 204l6 10 6-10"/>
</svg>

<!-- Step 3 -->
<p class="abs step-label" style="left:171px;top:2799px">STEP-3</p>
<h3 class="abs step-title" style="left:171px;top:2826px">Ready To Bake!</h3>
<p class="abs small" style="left:171px;top:2876px;width:430px;font-size:11.5px;line-height:20px">Once you've selected your ingredients, hit the BAKE button, and watch the magic happen. An iFrame popup will open, allowing you to play with the delicious results.</p>
<div class="abs grad solid" style="left:171px;top:2980px;width:158px;height:46px;font-size:18px">BAKE</div>
<div class="abs block" style="left:639px;top:2888px;width:388px;height:236px;background:linear-gradient(135deg,var(--yellow),var(--pink) 50%,var(--cyan))"></div>
<div class="abs pill" role="img" aria-label="Hands typing on a laptop" style="left:608px;top:2719px;width:172px;height:325px;background:linear-gradient(180deg,#3a2a22,#c9b8aa 50%,#f2efec)"></div>
<div class="abs pill" role="img" aria-label="Laptop showing analytics dashboard" style="left:806px;top:2772px;width:172px;height:323px;background:linear-gradient(180deg,#eef1f4,#b8c6d6 45%,#2a2d33)"></div>

<!-- FAQ -->
<p class="abs step-label" style="left:0;width:1200px;text-align:center;top:3206px;font-size:10px">FAQS</p>
<h2 class="abs section-title" style="left:0;width:1200px;top:3228px;font-size:26px">Frequently asked questions . . .</h2>
<div class="abs faq" style="top:3294px;height:147px">
  <div class="q">How does Morsel work if I don't give her my data ?<span class="sign">–</span></div>
  <p style="font-weight:400;font-size:9.5px;line-height:13px;width:380px;margin-top:18px">When you ask a question about structured data, the LLM can be very good at knowing how to answer the question.</p>
</div>
<div class="abs faq" style="top:3463px;height:45px"><div class="q" style="height:42px">How is Morsel different than QuillMate ?<span class="sign">+</span></div></div>
<div class="abs faq" style="top:3521px;height:45px"><div class="q" style="height:42px">How Accurate is Morsel ?<span class="sign">+</span></div></div>
<div class="abs btn-outline" style="left:537px;top:3603px;width:125px;height:28px;font-size:10.5px">View More FAQs</div>

<!-- Contact -->
<div class="abs" style="left:241px;top:3739px;width:716px;height:626px;border:1.5px solid #2a2a35;border-radius:50px"></div>
<h2 class="abs section-title" style="left:0;width:1200px;top:3786px;font-size:29px;color:#444">Get In Touch</h2>
<div class="abs field" style="top:3862px;height:117px;align-items:flex-start;padding-top:20px">Question ? FeedBack ? We Want it All.</div>
<div class="abs field" style="top:4013px;height:53px">John Smith</div>
<div class="abs field" style="top:4098px;height:53px">Email</div>
<div class="abs field" style="top:4184px;height:52px;justify-content:space-between">Describe your Organization
  <svg width="12" height="8" viewBox="0 0 12 8"><path d="M0 0h12L6 8z" fill="#16161d"/></svg></div>
<div class="abs solid" style="left:505px;top:4278px;width:188px;height:47px;font-size:19px;background:linear-gradient(90deg,#4a6fcf,#e58ac2)">Submit</div>

<!-- Footer -->
<div class="abs" style="left:84px;top:4420px;width:1032px;height:1px;background:#b9b3ba"></div>
<div class="abs brand" style="left:87px;top:4499px"><span class="brand-mark" style="width:40px;height:40px"></span><span class="brand-name" style="font-size:38px">loomberrys</span></div>
<svg class="abs" style="left:182px;top:4574px" width="86" height="28" viewBox="0 0 86 28" fill="none" stroke="#8a8a96" stroke-width="1.5">
  <circle cx="14" cy="14" r="12"/><circle cx="41" cy="14" r="12"/><circle cx="70" cy="14" r="12"/>
</svg>
<div class="foot">
  <h4 class="abs" style="left:608px;top:4474px">Quick Links</h4>
  <a class="abs" style="left:608px;top:4514px">Home</a><a class="abs" style="left:608px;top:4545px">About</a>
  <h4 class="abs" style="left:782px;top:4474px">Services</h4>
  <a class="abs" style="left:782px;top:4514px">Services</a><a class="abs" style="left:782px;top:4545px">Services</a>
  <h4 class="abs" style="left:958px;top:4474px">Others</h4>
  <a class="abs" style="left:958px;top:4514px">Terms of Service</a><a class="abs" style="left:958px;top:4545px">Privacy Policy</a><a class="abs" style="left:958px;top:4578px;font-size:10.5px">Loomberry API Disclosure</a>
</div>
<p class="abs" style="left:0;width:1200px;text-align:center;top:4628px;font-size:12.5px">© Company- All Rights Reserved</p>

</body>
</html>
```